New Company Business Card design

Looking for a corporate looking business card utilising my new logo design - the logo i would like embossed as one option and flat as another - simplistic but stylish - less is more - we are an import export business launching into the market - i would like a couple of options as main background - Grey or Black

```html
<!DOCTYPE html>
<html lang="en">
<head>
<meta charset="utf-8">
<title>Harbourline Trading – Business Cards</title>
<link href="https://fonts.googleapis.com/css2?family=Open+Sans:wght@400;600;700&display=swap" rel="stylesheet">
<style>
  :root {
    --stage: #4a4a4c;
    --stage-edge: #2b2b2d;
    --card: #1c1c1e;
    --card-tone: #2a2a2c;
    --brand-blue: #1f74c4;
    --text-light: #e6e6e6;
    --text-soft: #bdbdbd;
    --rule-blue: #1f74c4;
  }
  * { box-sizing: border-box; margin: 0; padding: 0; }
  html, body { width: 1200px; height: 1000px; overflow: hidden; }
  body {
    background: radial-gradient(ellipse at 55% 40%, var(--stage) 0%, var(--stage-edge) 100%);
    font-family: "Open Sans", Arial, sans-serif;
    position: relative;
  }
  .card {
    position: absolute;
    width: 640px;
    height: 366px;
    border-radius: 28px;
    overflow: hidden;
    box-shadow: 0 14px 30px rgba(0,0,0,0.45);
  }
  .card-surface {
    position: absolute; inset: 0;
    background: linear-gradient(135deg, var(--card-tone) 0%, var(--card) 60%, #151516 100%);
  }
  .card--front { left: 280px; top: 70px; }
  .card--back  { left: 280px; top: 520px; }

  .brand {
    position: absolute;
    display: flex; align-items: center; gap: 12px;
    color: var(--brand-blue);
    font-weight: 700;
    white-space: nowrap;
  }
  .brand-dot {
    border-radius: 50%;
    background: var(--brand-blue);
    flex: none;
  }
  .card--front .brand { left: 50%; top: 50%; transform: translate(-50%, -50%); font-size: 34px; }
  .card--front .brand-dot { width: 38px; height: 38px; }
  .card--back .brand { left: 42px; top: 120px; font-size: 24px; }
  .card--back .brand-dot { width: 28px; height: 28px; }

  .divider {
    position: absolute; left: 332px; top: 40px;
    width: 2px; height: 200px;
    background: var(--rule-blue);
  }
  .contact { position: absolute; left: 360px; top: 44px; color: var(--text-soft); }
  .contact-name { color: var(--brand-blue); font-size: 25px; font-weight: 600; line-height: 1.1; }
  .contact-role { font-size: 12.5px; margin-top: 4px; }
  .contact-lines { margin-top: 26px; display: grid; grid-template-columns: 22px auto; column-gap: 12px; row-gap: 14px; align-items: center; font-size: 13.5px; }
  .contact-lines p { line-height: 1.35; }
  .icon { width: 20px; height: 20px; }
  .address {
    position: absolute; left: 0; right: 0; bottom: 38px;
    text-align: center;
    color: var(--text-light);
    font-size: 20px;
  }
</style>
</head>
<body>
  <section class="card card--front" aria-label="Business card front">
    <div class="card-surface" role="img" aria-label="Dark carbon-weave textured card surface"></div>
    <div class="brand"><span class="brand-dot"></span>Harbourline Trading</div>
  </section>

  <section class="card card--back" aria-label="Business card back">
    <div class="card-surface" role="img" aria-label="Dark carbon-weave textured card surface"></div>
    <div class="brand"><span class="brand-dot"></span>Harbourline Trading</div>
    <div class="divider"></div>
    <div class="contact">
      <h1 class="contact-name">Dana Whitfield</h1>
      <p class="contact-role">Business Development Manager</p>
      <div class="contact-lines">
        <svg class="icon" viewBox="0 0 24 24" aria-hidden="true"><path fill="#1f74c4" d="M6.6 10.8a15.1 15.1 0 0 0 6.6 6.6l2.2-2.2a1 1 0 0 1 1-.25 11.4 11.4 0 0 0 3.6.57 1 1 0 0 1 1 1V20a1 1 0 0 1-1 1A17 17 0 0 1 3 4a1 1 0 0 1 1-1h3.5a1 1 0 0 1 1 1c0 1.25.2 2.45.57 3.57a1 1 0 0 1-.25 1z"/></svg>
        <p>+61 (0)7 5550 1234<br>+61 (0)7 5550 1288</p>
        <svg class="icon" viewBox="0 0 24 24" aria-hidden="true"><g fill="none" stroke="#1f74c4" stroke-width="1.6"><circle cx="12" cy="12" r="9"/><ellipse cx="12" cy="12" rx="4" ry="9"/><path d="M3 12h18M5 7h14M5 17h14"/></g></svg>
        <p>dwhitfield@harbourline.com.au<br>www.harbourline.com.au</p>
      </div>
    </div>
    <p class="address">12/88 Kestrel Park Road, Ashgrove QLD 4060</p>
  </section>
</body>
</html>
```